Business Card for Beach theme sports bar called TAVRU

I need a business card designed for our employees, front and back. This will be used by the employees of two business locations to hand out to customers. I've attached the previous business cards we used at one time for a Benwicks (it is now Tavru). Looking for a fresh new card that is elegant but has character.

Target Market(s)

30-60, middle class

Contact Information for Business Card

We are a beach bar and sports bar. I am looking for an elegant business card with the front to have the TAVRU logo. Then on the back I need it to allow a space for employees to write their names and for them to write in their schedule. I have attached our old cards with our old name Benwicks so you can pull everything we need on the cards. one thing is missing is we have another location at 2815 N Willow Crest Rd with a number of 702-418-9351. Since we will use it for both locations it should allow the employee to circle or check mark the bar which they work at.

Font styles to use
Sans Serif

Requirements
Must have
• We are looking for some fresh ideas for the business card. Something that will really stick out to customers when the staff hands them out. Creativity will be looked at positively, but we still want it to look upscale and fun.

```html
<!DOCTYPE html>
<html lang="en">
<head>
<meta charset="utf-8">
<title>Tavru Employee Business Card</title>
<link rel="stylesheet" href="https://fonts.googleapis.com/css2?family=Source+Sans+3:wght@400;600&display=swap">
<style>
  :root {
    --page: #e6e6e6;
    --ink: #000000;
    --paper: #ffffff;
    --shadow: rgba(0, 0, 0, 0.18);
  }
  * { margin: 0; padding: 0; box-sizing: border-box; }
  html, body {
    width: 1200px;
    height: 1111px;
    overflow: hidden;
    background: var(--page);
    font-family: "Source Sans 3", sans-serif;
  }
  .canvas { position: relative; width: 1200px; height: 1111px; }

  .card {
    position: absolute;
    overflow: hidden;
    background: var(--ink);
    box-shadow: 0 2px 6px var(--shadow);
  }

  /* Front */
  .card-front { left: 330px; top: 131px; width: 600px; height: 350px; }
  .front-disc {
    position: absolute;
    left: 123px; top: 9px;
    width: 354px; height: 354px;
    border-radius: 50%;
    background: var(--paper);
    display: flex;
    align-items: center;
    justify-content: center;
  }
  .brand-name {
    font-weight: 600;
    color: var(--ink);
    line-height: 1;
  }
  .front-disc .brand-name { font-size: 88px; margin-top: -10px; }

  /* Back */
  .card-back { left: 330px; top: 557px; width: 600px; height: 341px; }
  .back-panel { position: absolute; left: 0; top: 0; }

  .back-contact { position: absolute; left: 0; top: 0; width: 290px; color: var(--ink); }
  .back-contact .brand-name {
    position: absolute;
    left: 0; width: 270px;
    top: 78px;
    text-align: center;
    font-size: 40px;
  }

  .location {
    position: absolute;
    left: 32px;
    display: flex;
    align-items: flex-start;
    gap: 9px;
  }
  .location-first { top: 148px; }
  .location-second { top: 206px; }
  .location-mark {
    flex: none;
    width: 16px; height: 16px;
    margin-top: 2px;
    border: 2px solid var(--ink);
    border-radius: 50%;
  }
  .location-lines { font-size: 18px; line-height: 21px; font-weight: 400; }

  .employee-label {
    position: absolute;
    left: 379px; top: 84px;
    color: var(--paper);
    font-size: 24px;
    font-weight: 400;
  }

  .schedule {
    position: absolute;
    left: 300px; top: 198px;
    display: flex;
    gap: 9px;
  }
  .schedule-day {
    width: 34px;
    display: flex;
    flex-direction: column;
    align-items: center;
    color: var(--paper);
  }
  .schedule-day span { font-size: 23px; line-height: 1; height: 26px; }
  .schedule-day i {
    display: block;
    width: 34px; height: 32px;
    margin-top: 10px;
    background: var(--paper);
  }
</style>
</head>
<body>
<main class="canvas">

  <section class="card card-front" aria-label="Card front">
    <div class="front-disc">
      <span class="brand-name">Tavru</span>
    </div>
  </section>

  <section class="card card-back" aria-label="Card back">
    <svg class="back-panel" width="600" height="341" viewBox="0 0 600 341" aria-hidden="true">
      <path d="M0 0 H150 C250 25 300 110 290 190 C280 265 230 320 159 341 H0 Z" fill="#ffffff"/>
    </svg>

    <div class="back-contact">
      <span class="brand-name">Tavru</span>
      <div class="location location-first">
        <span class="location-mark" aria-hidden="true"></span>
        <p class="location-lines">702-418-9351<br>2815 N Willow Crest Rd</p>
      </div>
      <div class="location location-second">
        <span class="location-mark" aria-hidden="true"></span>
        <p class="location-lines">702-563-2084<br>5160 W Harbor Sands Ave</p>
      </div>
    </div>

    <p class="employee-label">Employe Name</p>

    <div class="schedule">
      <div class="schedule-day"><span>M</span><i></i></div>
      <div class="schedule-day"><span>T</span><i></i></div>
      <div class="schedule-day"><span>W</span><i></i></div>
      <div class="schedule-day"><span>TH</span><i></i></div>
      <div class="schedule-day"><span>F</span><i></i></div>
      <div class="schedule-day"><span>S</span><i></i></div>
      <div class="schedule-day"><span>Su</span><i></i></div>
    </div>
  </section>

</main>
</body>
</html>
```